Keratin Clear Clinic - Fungal Nails information booklet

We need an information booklet for a new company that diagnoses and treats fungal nail infections. Once the patient has been diagnosed with a fungal nail infection, we would like to provide them with a booklet (A5 size) that gives them a detailed understanding of what fungal nail infections are, how they get them, what treatment options are available etc. (please find attached the word doc with all of the information we would like included). We have also attached a link to a similar handout that we are after. We have also attached a copy of our logo design and our current letterhead which gives you an idea of the colours that we use. Finally, I have attached some images of before/after pics of our laser treatment, pictures of the laser etc. which we would like used in the laser treatment section of our booklet. The final design should communicate professional, minimalist and clean lined. Please note that we would like the ability to be able to edit the content at a later date if required.

Font styles to use
Serif

Requirements
Must have
• Pictures (feet, fungal nails) - as per handout which can be seen on the document uploaded (Guide_to_TNF_-_ENG_-_TIP_Brochure_-_FINAL_2_Print_Pages)

Before/after pics as per upload in the laser treatment section

```html
<!DOCTYPE html>
<html lang="en">
<head>
<meta charset="utf-8">
<title>Keratin Clear Clinic – Fungal Nails Booklet</title>
<link href="https://fonts.googleapis.com/css2?family=Cinzel:wght@500&family=Open+Sans:wght@400;600&display=swap" rel="stylesheet">
<style>
  :root {
    --brand-blue: #2f5ca3;
    --brand-blue-deep: #254a8c;
    --brand-blue-light: #4b76bd;
    --silver: #c3c7ce;
    --silver-light: #eceef1;
    --paper: #ffffff;
    --backdrop: #e6e7ea;
    --ink-light: #ffffff;
    --ink-dark: #1f2a3d;
    --ink-footer: #2f4f86;
    --skin: #e8c3ad;
    --towel: #efece8;
  }
  * { box-sizing: border-box; margin: 0; padding: 0; }
  html, body { width: 1200px; height: 900px; overflow: hidden; }
  body {
    background: var(--backdrop);
    font-family: "Open Sans", Arial, sans-serif;
    position: relative;
  }
  .page {
    position: absolute;
    width: 550px;
    height: 390px;
    top: 255px;
    overflow: hidden;
    box-shadow: 0 6px 18px rgba(0,0,0,0.18);
  }
  .page--cover { left: 30px; background: var(--paper); }
  .page--inside { left: 620px; background: var(--brand-blue); }
  .page__shapes { position: absolute; inset: 0; width: 100%; height: 100%; }

  .brand-name {
    position: absolute;
    font-family: "Cinzel", "Times New Roman", serif;
    font-weight: 500;
    color: var(--ink-light);
    text-align: center;
    line-height: 1.1;
  }
  .brand-name__main { display: block; letter-spacing: 1.5px; }
  .brand-name__sub { display: block; letter-spacing: 4px; }

  .page--cover .brand-name { left: 300px; top: 176px; width: 200px; }
  .page--cover .brand-name__main { font-size: 19px; }
  .page--cover .brand-name__sub { font-size: 11px; margin-top: 4px; }

  .partner-name {
    position: absolute;
    right: 20px;
    bottom: 26px;
    font-family: "Open Sans", Arial, sans-serif;
    font-weight: 600;
    font-size: 13px;
    color: var(--ink-dark);
  }

  .page--inside .brand-name { left: 36px; top: 48px; width: 230px; }
  .page--inside .brand-name__main { font-size: 20px; }
  .page--inside .brand-name__sub { font-size: 11px; margin-top: 4px; }

  .intro {
    position: absolute;
    left: 36px;
    top: 150px;
    width: 272px;
    font-size: 10px;
    line-height: 1.45;
    color: var(--ink-light);
  }
  .treatments {
    position: absolute;
    left: 36px;
    top: 232px;
    list-style: none;
    font-size: 10px;
    line-height: 2;
    color: var(--ink-light);
  }

  .contact-bar {
    position: absolute;
    left: 0; right: 0; bottom: 0;
    height: 34px;
    display: flex;
    justify-content: space-around;
    align-items: center;
    padding: 0 20px;
    font-size: 9px;
    color: var(--ink-footer);
  }
  .contact-bar__item { display: flex; align-items: center; gap: 6px; }
  .contact-bar__icon { width: 13px; height: 13px; }
</style>
</head>
<body>

<section class="page page--cover" aria-label="Booklet cover">
  <svg class="page__shapes" viewBox="0 0 550 390">
    <defs>
      <linearGradient id="feetPhoto" x1="0" y1="0" x2="1" y2="1">
        <stop offset="0" stop-color="#f3efea"/>
        <stop offset="0.45" stop-color="var(--skin)"/>
        <stop offset="1" stop-color="var(--towel)"/>
      </linearGradient>
      <linearGradient id="coverPanel" x1="0" y1="0" x2="1" y2="0">
        <stop offset="0" stop-color="#f2f3f5"/>
        <stop offset="1" stop-color="#ffffff"/>
      </linearGradient>
    </defs>
    <rect x="0" y="0" width="550" height="390" fill="url(#feetPhoto)" role="img" aria-label="Photo of bare feet resting on a white towel with pink orchid flowers"/>
    <circle cx="520" cy="190" r="262" fill="none" stroke="var(--silver)" stroke-width="8"/>
    <circle cx="520" cy="190" r="255" fill="url(#coverPanel)"/>
    <circle cx="400" cy="200" r="108" fill="var(--brand-blue)"/>
    <circle cx="460" cy="270" r="26" fill="var(--brand-blue-light)" opacity="0.25"/>
  </svg>
  <h1 class="brand-name">
    <span class="brand-name__main">KERATIN CLEAR</span>
    <span class="brand-name__sub">CLINIC</span>
  </h1>
  <p class="partner-name">Northwell Care</p>
</section>

<section class="page page--inside" aria-label="Booklet inside page">
  <svg class="page__shapes" viewBox="0 0 550 390">
    <defs>
      <linearGradient id="insideBg" x1="0" y1="0" x2="1" y2="1">
        <stop offset="0" stop-color="var(--brand-blue)"/>
        <stop offset="1" stop-color="var(--brand-blue-deep)"/>
      </linearGradient>
      <linearGradient id="silverPanel" x1="0" y1="0" x2="1" y2="0">
        <stop offset="0" stop-color="#cfd2d8"/>
        <stop offset="1" stop-color="#f4f5f7"/>
      </linearGradient>
      <linearGradient id="stretchPhoto" x1="0" y1="0" x2="0" y2="1">
        <stop offset="0" stop-color="#c9d3dc"/>
        <stop offset="0.55" stop-color="#6f8fa8"/>
        <stop offset="1" stop-color="#8a7a6a"/>
      </linearGradient>
    </defs>
    <rect width="550" height="390" fill="url(#insideBg)"/>
    <circle cx="600" cy="170" r="236" fill="none" stroke="var(--silver)" stroke-width="6"/>
    <circle cx="600" cy="170" r="230" fill="url(#silverPanel)"/>
    <circle cx="402" cy="80" r="18" fill="#ffffff" opacity="0.35"/>
    <circle cx="452" cy="186" r="90" fill="var(--brand-blue)"/>
    <circle cx="452" cy="186" r="78" fill="url(#stretchPhoto)" role="img" aria-label="Photo of a woman stretching against a railing on a seaside pier"/>
    <rect x="0" y="356" width="550" height="34" fill="var(--silver-light)"/>
  </svg>

  <h2 class="brand-name">
    <span class="brand-name__main">KERATIN CLEAR</span>
    <span class="brand-name__sub">CLINIC</span>
  </h2>

  <p class="intro">We are your experts at treating fungal nail infections and understand that fungal nail infections can reduce your confidence to wearing open toe shoes and bare feet due to thickened, yellow or irregularly shaped nails.</p>

  <ol class="treatments">
    <li>1. Topical Treatments</li>
    <li>2. Systemic or Oral Treatments (through GP prescription)</li>
    <li>3. Laser and Physical Treatments</li>
  </ol>

  <footer class="contact-bar">
    <span class="contact-bar__item">
      <svg class="contact-bar__icon" viewBox="0 0 14 14"><circle cx="7" cy="7" r="7" fill="var(--ink-footer)"/><rect x="3.5" y="4.5" width="7" height="5" fill="none" stroke="#fff" stroke-width="1"/><path d="M3.5 4.5 L7 7.3 L10.5 4.5" fill="none" stroke="#fff" stroke-width="1"/></svg>
      info@keratinclear.nz
    </span>
    <span class="contact-bar__item">
      <svg class="contact-bar__icon" viewBox="0 0 14 14"><circle cx="7" cy="7" r="7" fill="var(--ink-footer)"/><path d="M4.6 3.6 L6 5.2 L5.3 6.2 Q6.3 8 7.8 8.7 L8.8 8 L10.4 9.4 L9.6 10.5 Q6.5 10.2 3.6 4.6 Z" fill="#fff"/></svg>
      01 555 0142
    </span>
    <span class="contact-bar__item">
      <svg class="contact-bar__icon" viewBox="0 0 14 14"><circle cx="7" cy="7" r="7" fill="var(--ink-footer)"/><circle cx="7" cy="7" r="3.6" fill="none" stroke="#fff" stroke-width="0.9"/><path d="M3.4 7 H10.6 M7 3.4 Q5 7 7 10.6 M7 3.4 Q9 7 7 10.6" fill="none" stroke="#fff" stroke-width="0.8"/></svg>
      www.keratinclear.nz
    </span>
  </footer>
</section>

</body>
</html>
```